Post it Note design

POST-IT NOTE DESIGN (CONTENT)
Size recommended: 4x6 for handwriting space.
Header (Bold):
Lighting Issue Detected on Your Property
Sub-header:
During our routine night inspection, we noted the following item(s):
Checkbox List:
⬜ Building Lights Out
⬜ Pole Lights Out
⬜ Sign Not Illuminated
⬜ Other ________________________
Action Line:
We can provide a quote or dispatch service right away.
Area for notes
Contact Block (Bold & Centered):
Brovane Fixture Inc.
Service@BrovaneFixture.com
www.BrovaneFixture.com
877-514-0862
Industry/Entity Type
Electrical lighting
Colors
Designer to choose colors to be used in the design.
Look and feel
Each slider illustrates characteristics of the customer's brand and the style your logo design should communicate.

```html
<!DOCTYPE html>
<html lang="en">
<head>
<meta charset="utf-8">
<title>Brovane Fixture Inc. – Lighting Issue Note</title>
<link href="https://fonts.googleapis.com/css2?family=Montserrat:wght@400;500;600;700;800;900&display=swap" rel="stylesheet">
<style>
  :root {
    --red: #ed1c24;
    --navy: #283583;
    --ink: #111111;
    --paper: #ffffff;
    --backdrop: #a9a9a9;
  }
  * { margin: 0; padding: 0; box-sizing: border-box; }
  html, body { width: 1200px; height: 1200px; overflow: hidden; }
  body {
    background: var(--backdrop);
    font-family: 'Montserrat', sans-serif;
    position: relative;
  }
  .note {
    position: absolute;
    left: 254px; top: 81px;
    width: 692px; height: 1037px;
    background: var(--paper);
    overflow: hidden;
  }
  .brand-name {
    position: absolute;
    top: 63px; left: 0; width: 100%;
    text-align: center;
    color: var(--red);
    font-weight: 900;
    font-size: 56px;
    line-height: 1.1;
    letter-spacing: 1px;
    text-transform: uppercase;
  }
  .alert-band {
    position: absolute;
    top: 251px; left: 0; width: 100%; height: 126px;
    background: var(--red);
    border-top: 4px solid var(--navy);
    border-bottom: 4px solid var(--navy);
    display: flex; align-items: center; justify-content: center;
    text-align: center;
  }
  .alert-band h1 {
    color: #fff;
    font-weight: 800;
    font-size: 41px;
    line-height: 1.06;
    word-spacing: 5px;
    text-shadow: 2px 2px 3px rgba(0,0,0,0.35);
  }
  .intro {
    position: absolute;
    top: 391px; left: 0; width: 100%;
    text-align: center;
    color: var(--navy);
    font-size: 22.5px;
    font-weight: 500;
    line-height: 27px;
  }
  .intro strong { font-weight: 700; }
  .checklist {
    position: absolute;
    top: 475px; left: 37px;
    width: 608px;
    display: grid;
    grid-template-columns: 291px 291px;
    column-gap: 26px;
    row-gap: 25px;
    list-style: none;
  }
  .check-item {
    height: 42px;
    border: 1.5px solid var(--navy);
    border-radius: 5px;
    display: flex; align-items: center;
    padding-left: 9px;
    color: var(--navy);
    font-size: 22px;
    font-weight: 600;
    white-space: nowrap;
  }
  .check-box {
    width: 22px; height: 22px;
    border: 2px solid #333;
    margin-right: 12px;
    flex: none;
  }
  .fill-line {
    display: inline-block;
    width: 168px;
    border-bottom: 2px solid var(--navy);
    height: 20px;
  }
  .action-panel {
    position: absolute;
    top: 615px; left: 37px;
    width: 608px; height: 107px;
    background: var(--navy);
    border-radius: 10px;
    color: #fff;
    text-align: center;
    padding-top: 5px;
  }
  .action-lead, .action-tail {
    font-size: 25px; font-weight: 600; letter-spacing: -0.5px; line-height: 28px;
  }
  .action-tail { font-size: 26px; }
  .action-main {
    font-size: 44px; font-weight: 900; line-height: 40px;
    text-shadow: 2px 2px 3px rgba(0,0,0,0.45);
  }
  .notes {
    position: absolute;
    top: 730px; left: 40px; width: 601px;
  }
  .notes-row {
    height: 39px;
    display: flex; align-items: flex-end;
    font-size: 21px; color: var(--ink); font-weight: 500;
  }
  .notes-row .dots {
    flex: 1;
    border-bottom: 3px dotted #222;
    margin-bottom: 4px;
  }
  .contact {
    position: absolute;
    top: 866px; left: 0; width: 100%;
    text-align: center;
  }
  .contact-name {
    color: var(--navy); font-weight: 800; font-size: 45px; word-spacing: 10px; line-height: 48px;
  }
  .contact-phone {
    display: flex; align-items: center; justify-content: center; gap: 4px;
    color: var(--red); font-weight: 800; font-size: 46px; line-height: 46px;
  }
  .contact-phone svg { width: 28px; height: 28px; }
  .contact-line { font-size: 20px; font-weight: 500; color: var(--ink); line-height: 28px; }
  .contact-line .site { color: var(--navy); font-weight: 600; }
  .note-footer {
    position: absolute; bottom: 0; left: 0; width: 100%; height: 11px;
    display: flex;
  }
  .note-footer .red { flex: 1; background: var(--red); margin-right: 2px; }
  .note-footer .navy { flex: 1; background: var(--navy); }
</style>
</head>
<body>
  <main class="note">
    <div class="brand-name">Brovane Fixture<br>Inc.</div>

    <section class="alert-band">
      <h1>LIGHTING ISSUE DETECTED<br>ON YOUR PROPERTY</h1>
    </section>

    <p class="intro">DURING OUR <strong>ROUTINE NIGHT INSPECTION,</strong><br>WE NOTED THE FOLLOWING ITEM(S):</p>

    <ul class="checklist">
      <li class="check-item"><span class="check-box"></span>Building Lights Out</li>
      <li class="check-item"><span class="check-box"></span>Sign Not Illuminated</li>
      <li class="check-item"><span class="check-box"></span>Pole Lights Out</li>
      <li class="check-item"><span class="check-box"></span>Other<span class="fill-line"></span></li>
    </ul>

    <section class="action-panel">
      <div class="action-lead">WE CAN PROVIDE A</div>
      <div class="action-main">QUOTE OR DISPATCH</div>
      <div class="action-tail">SERVICE RIGHT AWAY</div>
    </section>

    <section class="notes">
      <div class="notes-row">NOTES<span class="dots"></span></div>
      <div class="notes-row"><span class="dots"></span></div>
      <div class="notes-row"><span class="dots"></span></div>
    </section>

    <section class="contact">
      <div class="contact-name">BROVANE FIXTURE INC.</div>
      <div class="contact-phone">
        <svg viewBox="0 0 24 24" aria-hidden="true">
          <path fill="#283583" d="M6.6 2.5c.6-.4 1.4-.2 1.8.4l2 3.2c.4.6.2 1.3-.3 1.7l-1.5 1.1c.8 2.2 2.3 4.1 4.3 5.4l1.3-1.3c.5-.5 1.300-.5 1.8 0l2.6 2.6c.5.5.5 1.3 0 1.8l-1.6 1.6c-1 1-2.6 1.2-3.9.5C8.5 17.2 5.3 13.4 3.8 8.9c-.4-1.3 0-2.8 1.1-3.7z"/>
          <path fill="none" stroke="#283583" stroke-width="1.5" stroke-linecap="round" d="M14 4.5a5.5 5.5 0 0 1 5 5M14 1.5a8.5 8.5 0 0 1 8 8"/>
        </svg>
        877-514-0862
      </div>
      <div class="contact-line">Service@BrovaneFixture.com</div>
      <div class="contact-line">www.<span class="site">BrovaneFixture</span>.com</div>
    </section>

    <div class="note-footer"><span class="red"></span><span class="navy"></span></div>
  </main>
</body>
</html>
```